New business card design to go with our new logo

just want an eye-catching business card to go with our new logo. We are open to double sided or single sided. Just want it to have the following info on it. Whatever layout you think looks best.

First and Last Name
Title
Phone 801-555-0187
Address 312 W. Larkmoor Avenue Orem UT 84057
Email thecrew@meadowstailandkennel.example

Industry/Entity Type

Business

```html
<!DOCTYPE html>
<html lang="en">
<head>
<meta charset="utf-8">
<title>Meadows Tail &amp; Kennel – Business Card</title>
<link rel="stylesheet" href="https://fonts.googleapis.com/css2?family=Lato:wght@400;700;900&display=swap">
<style>
  :root {
    --backdrop: #1b1c1c;
    --card: #ffffff;
    --brand-blue: #2ea3d8;
    --brand-orange: #f68d4b;
    --ink: #3a3a3a;
    --muted: #4a4a4a;
  }
  * { box-sizing: border-box; margin: 0; padding: 0; }
  html, body { width: 1200px; height: 1000px; overflow: hidden; }
  body {
    background: var(--backdrop);
    font-family: "Lato", Arial, sans-serif;
    display: flex;
    flex-direction: column;
    align-items: center;
    justify-content: center;
    gap: 60px;
  }
  .card {
    position: relative;
    width: 600px;
    height: 343px;
    background: var(--card);
    border-radius: 34px;
    overflow: hidden;
  }
  .card::after {
    content: "";
    position: absolute;
    left: 0; right: 0; bottom: 0;
    height: 9px;
  }
  .card--front::after { background: var(--brand-blue); }
  .card--back::after { background: var(--brand-orange); }

  /* Front */
  .brand {
    position: absolute;
    inset: 0 0 9px 0;
    display: flex;
    flex-direction: column;
    align-items: center;
    justify-content: center;
    gap: 22px;
  }
  .brand__dot {
    width: 120px; height: 120px;
    border-radius: 50%;
    border: 12px solid var(--brand-orange);
  }
  .brand__name {
    font-weight: 900;
    font-size: 40px;
    color: var(--brand-orange);
    letter-spacing: 0.5px;
  }

  /* Back */
  .contact {
    position: absolute;
    left: 40px; top: 42px;
    width: 330px;
    color: var(--ink);
  }
  .contact__name {
    font-weight: 900;
    font-size: 22px;
    color: var(--brand-blue);
    letter-spacing: 0.5px;
  }
  .contact__title {
    font-size: 18px;
    color: var(--muted);
    letter-spacing: 0.5px;
    margin-top: 2px;
  }
  .contact__address {
    font-size: 17px;
    line-height: 1.35;
    margin-top: 28px;
  }
  .contact__lines { list-style: none; margin-top: 26px; }
  .contact__line {
    display: flex;
    align-items: center;
    gap: 10px;
    font-size: 16px;
    line-height: 1.55;
    white-space: nowrap;
  }
  .contact__icon { width: 16px; height: 16px; flex: none; fill: var(--brand-blue); }
  .contact__icon--stroke { fill: none; stroke: var(--brand-blue); stroke-width: 1.6; }
  .emblem {
    position: absolute;
    right: 44px; top: 50%;
    transform: translateY(-50%);
    width: 200px; height: 200px;
    border-radius: 50%;
    border: 16px solid var(--brand-orange);
  }
</style>
</head>
<body>

  <section class="card card--front" aria-label="Card front">
    <div class="brand">
      <div class="brand__dot"></div>
      <div class="brand__name">Meadows Tail &amp; Kennel</div>
    </div>
  </section>

  <section class="card card--back" aria-label="Card back">
    <div class="contact">
      <h1 class="contact__name">DANA WHITFIELD</h1>
      <p class="contact__title">MANAGER</p>
      <p class="contact__address">312 W. Larkmoor Avenue,<br>Orem UT 84057</p>
      <ul class="contact__lines">
        <li class="contact__line">
          <svg class="contact__icon" viewBox="0 0 16 16" aria-hidden="true"><path d="M4 1h2.5l1 3.5-1.6 1.2a9 9 0 0 0 4.4 4.4l1.2-1.6 3.5 1V12a2.5 2.5 0 0 1-2.5 2.5A11 11 0 0 1 1.5 3.5 2.5 2.5 0 0 1 4 1z"/></svg>
          801-555-0187
        </li>
        <li class="contact__line">
          <svg class="contact__icon" viewBox="0 0 16 16" aria-hidden="true"><path d="M1 3h14v10H1z M1.5 3.5 8 9l6.5-5.5" /><path d="M1 3l7 5.8L15 3v1.4L8 10.2 1 4.4z" fill="#fff"/></svg>
          thecrew@meadowstailandkennel.example
        </li>
        <li class="contact__line">
          <svg class="contact__icon contact__icon--stroke" viewBox="0 0 16 16" aria-hidden="true"><circle cx="8" cy="8" r="6.5"/><ellipse cx="8" cy="8" rx="3" ry="6.5"/><path d="M1.5 8h13M2.5 4.8h11M2.5 11.2h11"/></svg>
          meadowstailandkennel.example
        </li>
      </ul>
    </div>
    <div class="emblem" aria-hidden="true"></div>
  </section>

</body>
</html>
```